Law Firm Logo and Stationary

I need a logo for my law firm.  The logo should only contain the firm name "Harlow & Harlow, P.C." but we are open to slight additions like underlining or a box.  We are looking for a modern style but not edgy because our target market is businesses and corporations.

I would like a logo that invokes the traditional values of a law firm (trust, integrity, knowledge) but I want an updated look.

To be clear, the logo should only contain the firm name, I am just looking for a font treatment.

The logo color is up to you.  The only initial opinion I have is that bright colors may not fit with the professional look of a law firm. 

I also want to incorporate the new logo into letterhead and business card designs.  The letterhead should include all of the information that is in my current letterhead, which is attached.  The letterhead should be black or grey on white.  The colored logo will go on the website and promotional materials.

For the business card, I would like to have the logo on the top left, the employee name (Colin J. Harlow) on the middle left and the firm information (address, tel, fax, website, email) on right side.  I am open to suggestions if you have better ideas.
Updates

Here are some comments on the initial 8 designs:

a) I am just interested in a font treatment of our firm name, "Harlow & Harlow, P.C."  I do not want any graphics like a gavel or shield. 

b) The full name of the firm must be in the logo.  So I cannot use designs that only have "H & H"

c) EXAMPLES: Here are two websites with examples of law firm logos that just have the firm name.  These are just samples to give you a general idea of what I am looking for.  Check out:  www.qx-legalco.com and www.tarrowmeade-law.com 

In short, I am looking for a simple, clean design that will look modern enough for our website but is also conservative enough to be on letterhead that gets sent to judges and other lawyers.

Also, the sample letterhead is now loaded in the brief so you can see the information I need included in the new letterhead.

Thanks.

Target Market(s)

businesses and corporations.

Industry/Entity Type

Law Firm

Logo Text

Harlow & Harlow, P.C.

Requirements
Must have
• Firm name, "Harlow & Harlow, P.C."

```html
<!DOCTYPE html>
<html lang="en">
<head>
<meta charset="utf-8">
<title>Harlow &amp; Harlow, P.C. — Letterhead and Business Card</title>
<link rel="stylesheet" href="https://fonts.googleapis.com/css2?family=Roboto+Condensed:wght@700&family=Questrial&display=swap">
<style>
  :root {
    --ink: #1d1d1d;
    --brand-brown: #5d534b;
    --band-brown: #5b4c43;
    --accent-orange: #f05a2a;
    --muted: #6b625a;
    --paper: #ffffff;
    --black: #000000;
  }
  * { margin: 0; padding: 0; box-sizing: border-box; }
  html, body { width: 927px; height: 1200px; overflow: hidden; background: var(--paper); }
  body { position: relative; font-family: "Questrial", "Helvetica Neue", Arial, sans-serif; color: var(--ink); }

  .wordmark { font-family: "Roboto Condensed", "Arial Narrow", sans-serif; font-weight: 700; color: var(--brand-brown); white-space: nowrap; letter-spacing: -0.5px; line-height: 1; }
  .label { font-family: "Roboto Condensed", "Arial Narrow", sans-serif; font-weight: 700; }

  /* Letterhead header */
  .letterhead-logo { position: absolute; left: 20px; top: 14px; font-size: 60px; }
  .letterhead-sub { position: absolute; left: 22px; top: 80px; font-size: 27px; color: var(--black); line-height: 1; }

  .attorneys { position: absolute; right: 29px; top: 24px; text-align: right; font-size: 18px; line-height: 26px; color: var(--ink); }
  .admissions { position: absolute; right: 29px; top: 121px; text-align: right; font-size: 18px; line-height: 26px; }
  .admissions .jurisdiction { color: var(--muted); }
  .admissions .jurisdiction.strong { color: var(--ink); font-weight: 700; font-family: "Roboto Condensed", "Arial Narrow", sans-serif; }

  /* Business card — back */
  .card-back { position: absolute; left: 476px; top: 367px; width: 425px; height: 219px; background: var(--accent-orange); }
  .card-back .wordmark { position: absolute; left: 0; right: 0; top: 78px; text-align: center; font-size: 40px; }
  .card-back .web { position: absolute; left: 0; right: 0; top: 127px; text-align: center; color: var(--paper); font-size: 14px; }

  /* Business card — front */
  .card-front { position: absolute; left: 351px; top: 200px; width: 425px; height: 241px; background: var(--paper); border: 1.5px solid #8a8580; }
  .card-front .wordmark { position: absolute; left: 0; right: 0; top: 14px; text-align: center; font-size: 38px; }
  .card-front .sub { position: absolute; left: 0; right: 0; top: 55px; text-align: center; font-size: 15px; color: var(--accent-orange); }
  .card-front .rule { position: absolute; left: 0; right: 0; top: 76px; height: 9px; background: var(--band-brown); }
  .card-front .holder { position: absolute; left: 8px; top: 94px; }
  .card-front .holder .name { font-size: 16px; color: var(--accent-orange); }
  .card-front .holder .fine { font-size: 9.5px; line-height: 13px; margin-top: 3px; }
  .card-front .holder .email-label { font-size: 14px; color: var(--accent-orange); margin-top: 17px; }
  .card-front .holder .email { font-size: 13px; margin-top: 3px; }
  .card-front .details { position: absolute; right: 8px; top: 94px; text-align: right; font-size: 13px; line-height: 19px; }
  .card-front .details .label { color: var(--accent-orange); font-size: 14px; }

  /* Letterhead footer */
  .footer-rule { position: absolute; left: 0; top: 1080px; width: 927px; height: 27px; background: var(--black); }
  .footer { position: absolute; left: 0; top: 1107px; width: 927px; height: 93px; background: var(--band-brown); color: var(--paper); text-align: center; font-size: 16px; line-height: 27px; padding-top: 24px; }
</style>
</head>
<body>
  <header>
    <div class="wordmark letterhead-logo">HARLOW &amp; HARLOW P.C.</div>
    <div class="label letterhead-sub">LAW OFFICES</div>

    <div class="attorneys">
      <div>MARTIN E. HARLOW † #</div>
      <div>COLIN J. HARLOW † *</div>
      <div>SAMUEL HARLOW (1916-1994)</div>
    </div>

    <div class="admissions">
      <div>ADMITTED TO PRACTICE</div>
      <div class="jurisdiction">†District of Columbia</div>
      <div class="jurisdiction">#Maryland</div>
      <div class="jurisdiction strong">*New York</div>
    </div>
  </header>

  <section class="card-back" aria-label="Business card back">
    <div class="wordmark">HARLOW &amp; HARLOW P.C.</div>
    <div class="label web">WWW.HARLOWPC.COM</div>
  </section>

  <section class="card-front" aria-label="Business card front">
    <div class="wordmark">HARLOW &amp; HARLOW P.C.</div>
    <div class="label sub">LAW OFFICES</div>
    <div class="rule"></div>
    <div class="holder">
      <div class="label name">COLIN J. HARLOW † *</div>
      <div class="fine">Admitted to Practice<br>†District of Columbia<br>*New York</div>
      <div class="label email-label">EMAIL</div>
      <div class="email">colin.harlow@harlowpc.com</div>
    </div>
    <div class="details">
      <div class="label">ADDRESSES</div>
      <div>2170 Alder Avenue</div>
      <div>Fairhaven, MD 20915</div>
      <div class="label">PHONE</div>
      <div>301.555.0142</div>
      <div class="label">FAX</div>
      <div>301.555.0178</div>
    </div>
  </section>

  <div class="footer-rule"></div>
  <footer class="footer">
    <div>ADDRESSES | 2170 Alder Avenue | Fairhaven, MD 20915 PHONE | 301.555.0142 FAX | 301.555.0178</div>
    <div>WEB | www.harlowpc.com EMAIL | colin.harlow@harlowpc.com</div>
  </footer>
</body>
</html>
```